Corwin Ashgrove

I am a songwriter and would like to include a bio, pictures, discography, CD covers and access to some of my music

Target Market(s)

Music Lovers, songwriters publishers

Coding

Coded - Design and coding required

Number of Pages Required

5+ page

Requirements
Must have
• Pictures of my CD covers, pictures of me and either my Music or links to my music
Nice to have
Should not have
• cartoons

```html
<!DOCTYPE html>
<html lang="en">
<head>
<meta charset="utf-8">
<title>Corwin Ashgrove — Songwriter</title>
<link rel="stylesheet" href="https://fonts.googleapis.com/css2?family=Abril+Fatface&family=Playfair+Display:wght@400;700&family=Roboto:ital,wght@0,400;0,500;0,700;1,400;1,500&display=swap">
<style>
:root{
  --red:#c4121b;
  --red-dark:#7d0b12;
  --black:#000;
  --footer:#161616;
  --text:#e6e6e6;
  --muted:#bdbdbd;
  --line:#8a8a8a;
}
*{box-sizing:border-box;margin:0;padding:0}
html,body{width:1200px;height:4539px;overflow:hidden;background:var(--black)}
body{position:relative;font-family:"Roboto",Arial,sans-serif;color:var(--text)}
.abs{position:absolute}
.section{position:absolute;left:0;width:1200px;overflow:hidden}
.display{font-family:"Abril Fatface",Georgia,serif;color:#fff;font-weight:400;letter-spacing:.5px}
.title{left:0;width:1200px;text-align:center;font-size:36px;line-height:40px}
.rule{height:3px;width:70px;left:565px;background:var(--red)}
.btn{position:absolute;display:flex;align-items:center;justify-content:center;gap:7px;background:var(--red);color:#fff;border-radius:25px;font-size:15px;font-weight:700;text-transform:uppercase;letter-spacing:.3px;white-space:nowrap}
.brand{font-family:"Playfair Display",Georgia,serif;color:var(--red);font-size:26px;font-weight:400;letter-spacing:1px;text-transform:uppercase;white-space:nowrap}
.brand-dot{width:14px;height:14px;border-radius:50%;background:var(--red)}
.social{width:39px;height:39px;border-radius:50%;background:#fff;top:36px}
.nav{top:106px;font-size:15px;font-weight:500;color:#fff;white-space:nowrap}
.hero-bg{left:0;top:0;width:1200px;height:599px;background:
  radial-gradient(ellipse 520px 260px at 200px 520px,#ff8a1e 0%,#d94a0a 35%,rgba(60,10,0,0) 75%),
  radial-gradient(ellipse 300px 200px at 1100px 480px,#e5570f 0%,rgba(60,10,0,0) 70%),
  radial-gradient(ellipse 230px 330px at 720px 360px,#c9b8a6 0%,#5a4a42 45%,rgba(0,0,0,0) 75%),
  linear-gradient(180deg,#0a0707 0%,#1b0d08 45%,#5a1c06 100%)}
.dot{width:10px;height:10px;border-radius:50%;background:#fff;top:555px}
.dot.active{width:16px;height:16px;top:552px}
.about-photo{left:97px;top:722px;width:414px;height:332px;border-radius:50%;background:radial-gradient(ellipse at 55% 40%,#e6d6c4 0%,#a58a66 45%,#6c5234 100%)}
.stage-bg{background:radial-gradient(ellipse 600px 300px at 600px 80px,#5c6168 0%,#262a30 45%,#0b0b0d 100%)}
.cover{width:310px;height:229px;overflow:hidden}
.cover .art{position:absolute;left:0;top:0;width:100%;height:100%}
.cover .label{position:absolute;left:0;bottom:0;width:100%;height:36px;background:var(--red-dark);display:flex;align-items:center;justify-content:center;color:#fff;font-weight:700;font-size:17px;text-transform:uppercase;white-space:nowrap}
.feature-panel{background:var(--red-dark);text-align:center;color:#fff}
.feature-panel h3{font-size:20px;font-weight:500;margin-top:10px}
.feature-panel p{font-size:13px;line-height:26px;margin:10px 22px 0}
.quote{font-size:14px;line-height:28.2px;font-style:italic;font-weight:500;text-align:justify;color:#fff}
.gtile{width:229px;height:229px}
.disc{width:176px;height:176px;border-radius:50%;border:3px solid #d8d8d8;top:3684px;padding:6px;background:#000}
.disc .art{width:100%;height:100%;border-radius:50%}
.play{width:36px;height:36px;border-radius:50%;background:#fff;top:3754px;display:flex;align-items:center;justify-content:center}
.album{top:3872px;width:220px;text-align:center;color:#fff}
.album .year{font-size:17px}
.album h4{font-size:18px;font-weight:700;margin-top:8px}
.album .sub{font-size:13px;margin-top:4px;color:var(--text)}
.mini{width:28px;height:28px;border-radius:50%;border:1.5px solid #cfcfcf;top:3965px;display:flex;align-items:center;justify-content:center}
.footer{top:4167px;height:372px;background:var(--footer)}
.fhead{font-size:15px;font-weight:700;color:#fff}
.flink{font-size:12px;color:var(--text);white-space:nowrap}
p.flink{white-space:normal}
</style>
</head>
<body>

<section class="section" style="top:0;height:599px">
  <div class="abs hero-bg" role="img" aria-label="Photo of the songwriter standing in front of a glowing fire crater at night"></div>

  <div class="abs brand-dot" style="left:226px;top:56px"></div>
  <div class="abs brand" style="left:111px;top:98px">Corwin Ashgrove</div>

  <div class="abs social" style="left:654px" aria-label="Social link"></div>
  <div class="abs social" style="left:703px" aria-label="Social link"></div>
  <div class="abs social" style="left:751px" aria-label="Social link"></div>
  <div class="abs social" style="left:799px" aria-label="Social link"></div>
  <div class="btn" style="left:858px;top:30px;width:229px;height:49px">♫ Download Songs</div>

  <div class="abs nav" style="left:465px">About Corwin Ashgrove</div>
  <div class="abs nav" style="left:668px">Gallery</div>
  <div class="abs nav" style="left:765px">Discography</div>
  <div class="abs nav" style="left:900px">Cd Covers</div>
  <div class="abs nav" style="left:1017px">My Music</div>

  <h1 class="abs display" style="left:111px;top:262px;font-size:44px;line-height:48px">DISCOVER THE MAGIC<br>OF MUSIC</h1>
  <div class="btn" style="left:111px;top:374px;width:190px;height:49px">♫ Get Started</div>

  <div class="abs dot" style="left:558px"></div>
  <div class="abs dot" style="left:575px"></div>
  <div class="abs dot active" style="left:592px"></div>
  <div class="abs dot" style="left:615px"></div>
  <div class="abs dot" style="left:632px"></div>
</section>

<section class="section" style="top:599px;height:578px;background:var(--black)"></section>
<div class="abs about-photo" role="img" aria-label="Portrait of the songwriter outdoors against a sandstone wall"></div>
<svg class="abs" style="left:90px;top:712px" width="430" height="352" viewBox="0 0 430 352" aria-hidden="true">
  <path d="M30 250 C0 140 90 30 215 14 C300 4 360 30 380 60 C330 30 250 22 180 40 C80 70 20 160 30 250Z" fill="#000"/>
  <path d="M70 300 C150 350 300 345 390 260 C330 320 180 340 70 300Z" fill="#000"/>
</svg>
<div class="abs" style="left:579px;top:682px;width:2px;height:410px;background:var(--line)"></div>
<h2 class="abs display" style="left:625px;top:700px;font-size:36px;line-height:45px">ABOUT<br>CORWIN ASHGROVE</h2>
<p class="abs" style="left:625px;top:800px;width:455px;font-size:14px;line-height:28px;text-align:justify;color:var(--text)">Corwin Ashgrove was born and raised in Houston, Texas. He began playing music at the age of eight when his sister returned home from summer camp and asked her parents to buy her a baritone ukulele. She taught her younger brother some chords on the ukulele and he was hooked. The following spring, they went to one of the border towns in Mexico and bought a Mexican guitar for $12. They restrung it with nylon strings</p>
<div class="btn" style="left:625px;top:1018px;width:182px;height:48px">♫ Learn More</div>

<section class="section stage-bg" style="top:1177px;height:837px" role="img" aria-label="Concert crowd under stage lights"></section>
<h2 class="abs display title" style="top:1257px">CD COVERS</h2>
<div class="abs rule" style="top:1312px"></div>

<div class="abs" style="left:111px;top:1353px;width:310px;height:243px;background:linear-gradient(135deg,#3ad16b,#e4e04a 40%,#d45ab0 70%,#2a8ae0)" role="img" aria-label="Album cover: musician with guitar in vivid psychedelic colours"></div>
<div class="abs feature-panel" style="left:111px;top:1596px;width:310px;height:244px">
  <svg style="margin-top:32px" width="48" height="48" viewBox="0 0 48 48" aria-hidden="true">
    <circle cx="22" cy="26" r="18" fill="none" stroke="#fff" stroke-width="2"/>
    <circle cx="22" cy="26" r="8" fill="none" stroke="#fff" stroke-width="2"/>
    <circle cx="22" cy="26" r="2" fill="#fff"/>
    <path d="M38 4 v14 M38 4 l8 3" stroke="#fff" stroke-width="2" fill="none"/>
    <circle cx="35" cy="18" r="3" fill="#fff"/>
  </svg>
  <h3>THE ASHGROVES</h3>
  <p>Lorem ipsum dolor sit amet, tetur adipiscing elit, sed do eiusmod temp cididunt ut labore et dolore magna aliqua.</p>
</div>

<div class="abs cover" style="left:446px;top:1353px">
  <div class="art" style="background:linear-gradient(160deg,#f2a21c,#d2361a 45%,#3a2a24 80%)" role="img" aria-label="Album cover: flames over a diner table with coffee cup"></div>
  <div class="label">Tam Wexford</div>
</div>
<div class="abs cover" style="left:779px;top:1353px">
  <div class="art" style="background:linear-gradient(180deg,#1a1a1a,#6a6a6a 55%,#222)" role="img" aria-label="Album cover: black and white guitarist in a hat with track list"></div>
  <div class="label">Sevrin Ashgrove</div>
</div>
<div class="abs cover" style="left:446px;top:1609px">
  <div class="art" style="background:linear-gradient(180deg,#5c6470,#2b2f36 55%,#7a3a20)" role="img" aria-label="Album cover: silhouette under lightning storm"></div>
  <div class="label">Restless Seasons</div>
</div>
<div class="abs cover" style="left:779px;top:1609px">
  <div class="art" style="background:linear-gradient(180deg,#7fa3b8,#3f6077 50%,#c9d6dc)" role="img" aria-label="Album cover: ship on stormy sea waves"></div>
  <div class="label">When The Tide Rolls In</div>
</div>
<div class="btn" style="left:476px;top:1877px;width:248px;height:47px">♫ View More Cover Art</div>

<div class="abs" style="left:0;top:2100px;width:1200px;text-align:center;color:var(--red);font-size:15px">TESTIMONIALS</div>
<h2 class="abs display title" style="top:2138px">FROM THE COMMUNITY</h2>
<div class="abs rule" style="top:2196px"></div>

<div class="abs display" style="left:83px;top:2222px;color:var(--red);font-size:46px;line-height:46px">“</div>
<p class="abs quote" style="left:83px;top:2272px;width:550px">Yet another great song from Corwin! An unlimited catalog of excellent work. Pleasure every time Yet another great experience! 5 stars, as always. Always a great day for me when I have one of Corwin's songs on my calendar. Thoroughly enjoy each one every time! Yet another great project from Corwin! I'm amazed at the breadth of his catalog. Always enjoyable working on his music! Corwin is quickly becoming one of my favorite clients (can I say that?) Smooth process every time, friendly exchanges, and great music to work on.</p>
<div class="abs display" style="left:505px;top:2460px;color:var(--red);font-size:46px;line-height:46px">”</div>
<div class="abs" style="left:83px;top:2489px;font-size:14px;font-weight:700;color:#fff;white-space:nowrap">Lena Marchetti Keyboards <span style="color:var(--red);margin-left:8px;letter-spacing:1px">★★★★★</span></div>
<div class="abs" style="left:666px;top:2243px;width:2px;height:307px;background:var(--line)"></div>
<div class="abs" style="left:705px;top:2255px;width:416px;height:330px;border-radius:50%;background:radial-gradient(ellipse at 50% 45%,#e8e8e8 0%,#8c8c8c 40%,#2a2a2a 80%)" role="img" aria-label="Black and white photo of a guitarist in a hat"></div>
<div class="abs dot" style="left:558px;top:2591px"></div>
<div class="abs dot" style="left:575px;top:2591px"></div>
<div class="abs dot" style="left:592px;top:2591px;background:var(--red)"></div>
<div class="abs dot" style="left:615px;top:2591px"></div>
<div class="abs dot" style="left:632px;top:2591px"></div>

<section class="section stage-bg" style="top:2678px;height:837px" role="img" aria-label="Concert crowd under stage lights"></section>
<h2 class="abs display title" style="top:2757px">OUR GALLERY</h2>
<div class="abs rule" style="top:2815px"></div>

<div class="abs gtile" style="left:111px;top:2854px;background:linear-gradient(135deg,#e25aa8,#6fd06a 45%,#e9d54c)" role="img" aria-label="Colourful portrait with guitar"></div>
<div class="abs gtile" style="left:359px;top:2866px;height:217px;background:linear-gradient(180deg,#1a0f0a,#6a4030 50%,#e2580f)" role="img" aria-label="Songwriter at the fire crater"></div>
<div class="abs gtile" style="left:608px;top:2854px;background:linear-gradient(180deg,#a8b7c0,#6c7a68 50%,#2c332e)" role="img" aria-label="Portrait by a lake"></div>
<div class="abs gtile" style="left:856px;top:2866px;height:217px;background:linear-gradient(180deg,#b59a76,#d8cbb8 55%,#e9e4dc)" role="img" aria-label="Portrait by a sandstone wall"></div>
<div class="abs gtile" style="left:111px;top:3098px;background:linear-gradient(180deg,#6b7078,#2c2e33 60%,#7a3b1e)" role="img" aria-label="Album art with lightning and silhouette"></div>
<div class="abs gtile" style="left:359px;top:3098px;background:linear-gradient(160deg,#f2a21c,#d2361a 45%,#d8cfc4)" role="img" aria-label="Album art with flames and diner table"></div>
<div class="abs gtile" style="left:608px;top:3098px;background:linear-gradient(180deg,#6c8c52,#d6c9b2 55%,#f3f3f3)" role="img" aria-label="Portrait in a cowboy hat"></div>
<div class="abs gtile" style="left:856px;top:3098px;background:linear-gradient(180deg,#6f8fb5,#e2dcc8 45%,#d7b8c8)" role="img" aria-label="Album art with childhood photo collage"></div>
<div class="btn" style="left:477px;top:3383px;width:245px;height:47px">♫ View More Pictures</div>

<h2 class="abs display title" style="top:3594px">DISCOGRAPHY</h2>
<div class="abs rule" style="top:3652px"></div>

<div class="abs disc" style="left:127px"><div class="art" style="background:radial-gradient(circle,#d5a0c8,#7a3d8f 60%,#2a1a3a)" role="img" aria-label="Album art: colourful guitarist"></div></div>
<div class="abs disc" style="left:382px"><div class="art" style="background:radial-gradient(circle,#8a8f96,#3a3e44 60%,#141518)" role="img" aria-label="Album art: storm and silhouette"></div></div>
<div class="abs disc" style="left:640px"><div class="art" style="background:radial-gradient(circle,#b48a5a,#5c3a22 60%,#1e140c)" role="img" aria-label="Album art: painted landscape with text"></div></div>
<div class="abs disc" style="left:895px"><div class="art" style="background:radial-gradient(circle,#d8d0c0,#8a94a8 60%,#3c4458)" role="img" aria-label="Album art: childhood photo collage"></div></div>

<div class="abs play" style="left:197px"><svg width="14" height="14" viewBox="0 0 14 14"><path d="M3 1 L13 7 L3 13Z" fill="#000"/></svg></div>
<div class="abs play" style="left:452px"><svg width="14" height="14" viewBox="0 0 14 14"><path d="M3 1 L13 7 L3 13Z" fill="#000"/></svg></div>
<div class="abs play" style="left:710px"><svg width="14" height="14" viewBox="0 0 14 14"><path d="M3 1 L13 7 L3 13Z" fill="#000"/></svg></div>
<div class="abs play" style="left:965px"><svg width="14" height="14" viewBox="0 0 14 14"><path d="M3 1 L13 7 L3 13Z" fill="#000"/></svg></div>

<div class="abs album" style="left:105px"><div class="year">2015</div><h4>LOREM IPSUM</h4><div class="sub">Lorem ipsum dolor sit amet,</div></div>
<div class="abs album" style="left:360px"><div class="year">2015</div><h4>LOREM IPSUM</h4><div class="sub">Lorem ipsum dolor sit amet,</div></div>
<div class="abs album" style="left:618px"><div class="year">2015</div><h4>LOREM IPSUM</h4><div class="sub">Lorem ipsum dolor sit amet,</div></div>
<div class="abs album" style="left:873px"><div class="year">2015</div><h4>LOREM IPSUM</h4><div class="sub">Lorem ipsum dolor sit amet,</div></div>

<div class="abs mini" style="left:159px"><svg width="10" height="10"><circle cx="5" cy="5" r="4" fill="#cfcfcf"/></svg></div>
<div class="abs mini" style="left:201px"><svg width="10" height="10"><path d="M2 1 L9 5 L2 9Z" fill="#cfcfcf"/></svg></div>
<div class="abs mini" style="left:243px"><svg width="12" height="12"><path d="M6 1 V8 M3 5 L6 8 L9 5 M2 11 H10" stroke="#cfcfcf" stroke-width="1.5" fill="none"/></svg></div>
<div class="abs mini" style="left:414px"><svg width="10" height="10"><circle cx="5" cy="5" r="4" fill="#cfcfcf"/></svg></div>
<div class="abs mini" style="left:456px"><svg width="10" height="10"><path d="M2 1 L9 5 L2 9Z" fill="#cfcfcf"/></svg></div>
<div class="abs mini" style="left:498px"><svg width="12" height="12"><path d="M6 1 V8 M3 5 L6 8 L9 5 M2 11 H10" stroke="#cfcfcf" stroke-width="1.5" fill="none"/></svg></div>
<div class="abs mini" style="left:672px"><svg width="10" height="10"><circle cx="5" cy="5" r="4" fill="#cfcfcf"/></svg></div>
<div class="abs mini" style="left:714px"><svg width="10" height="10"><path d="M2 1 L9 5 L2 9Z" fill="#cfcfcf"/></svg></div>
<div class="abs mini" style="left:756px"><svg width="12" height="12"><path d="M6 1 V8 M3 5 L6 8 L9 5 M2 11 H10" stroke="#cfcfcf" stroke-width="1.5" fill="none"/></svg></div>
<div class="abs mini" style="left:927px"><svg width="10" height="10"><circle cx="5" cy="5" r="4" fill="#cfcfcf"/></svg></div>
<div class="abs mini" style="left:969px"><svg width="10" height="10"><path d="M2 1 L9 5 L2 9Z" fill="#cfcfcf"/></svg></div>
<div class="abs mini" style="left:1011px"><svg width="12" height="12"><path d="M6 1 V8 M3 5 L6 8 L9 5 M2 11 H10" stroke="#cfcfcf" stroke-width="1.5" fill="none"/></svg></div>

<div class="btn" style="left:506px;top:4035px;width:188px;height:48px">♫ Play More</div>

<footer class="section footer">
  <div class="abs brand-dot" style="left:226px;top:118px"></div>
  <div class="abs brand" style="left:111px;top:160px">Corwin Ashgrove</div>
  <p class="abs flink" style="left:111px;top:204px;width:330px;line-height:20px">Lorem ipsum dolor sit amet, consectetur adipiscing elit, sed do eiusmod tempor incididunt</p>
  <div class="abs" style="left:111px;top:249px;width:123px;height:39px;border-radius:20px;background:var(--red);color:#fff;font-size:13px;font-weight:500;display:flex;align-items:center;justify-content:center">Ask Question</div>

  <div class="abs fhead" style="left:513px;top:62px">Quick Links</div>
  <div class="abs flink" style="left:513px;top:106px">About Corwin Ashgrove</div>
  <div class="abs flink" style="left:513px;top:136px">Gallery</div>
  <div class="abs flink" style="left:513px;top:166px">Discography</div>
  <div class="abs flink" style="left:513px;top:196px">Cd Covers</div>
  <div class="abs flink" style="left:513px;top:226px">My Music</div>

  <div class="abs fhead" style="left:707px;top:62px">Connect With US</div>
  <div class="abs flink" style="left:707px;top:106px">Fanpage</div>
  <div class="abs flink" style="left:707px;top:136px">Video Channel</div>
  <div class="abs flink" style="left:707px;top:166px">Photo Stream</div>
  <div class="abs flink" style="left:707px;top:196px">Pin Boards</div>

  <div class="abs fhead" style="left:916px;top:62px">Contact Us</div>
  <p class="abs flink" style="left:916px;top:104px;width:190px;line-height:20px">Feel free get in touch with us via phone or send us a message</p>
  <div class="abs flink" style="left:916px;top:156px;font-weight:700;color:#fff">555-014-2290</div>
  <div class="abs flink" style="left:916px;top:174px;font-weight:700;color:#fff">info@CorwinAshgrove.com</div>

  <div class="abs" style="left:111px;top:308px;width:978px;height:1px;background:#555"></div>
  <div class="abs flink" style="left:0;top:332px;width:1200px;text-align:center">Corwin Ashgrove Copyright © All right reserved</div>
</footer>

</body>
</html>
```